Amaranth an Quinoa Instant Flour - Packaging Design for Velmora Marketplace

I need a package design for the product that I have to sell on Velmora.

The current design needs to be adjusted to the US market.

Target Market(s)

velmora marketplace

Industry/Entity Type

Alimenticia

Font styles to use
Decorative

Colors
F0912C
F2A743
F7CA91
FBE8D2
FDF5EE

Requirements
Must have
• Design appropriate to the type of market to which it is directed
Nice to have
• A design suitable for Velmora

```html
<!DOCTYPE html>
<html lang="en">
<head>
<meta charset="utf-8">
<title>Granelle Amaranth and Quinoa Flour – Pack Front</title>
<link rel="stylesheet" href="https://fonts.googleapis.com/css2?family=Fredoka:wght@600;700&family=Gochi+Hand&family=Fira+Sans+Condensed:wght@700&display=swap">
<style>
  :root {
    --purple-deep: #4b2866;
    --purple: #52286f;
    --purple-ink: #5b2a86;
    --gold-light: #fbc744;
    --gold: #f5b53a;
    --gold-dark: #e59a22;
    --gold-rim: #f7d36a;
    --mauve: #9a4f80;
    --white: #ffffff;
    --cream: #fdf5ee;
    --drink-light: #d9b49a;
    --drink-dark: #8a5a43;
    --pod: #7a3f4a;
  }
  * { margin: 0; padding: 0; box-sizing: border-box; }
  html, body { width: 894px; height: 1200px; overflow: hidden; background: var(--white); }
  .pack {
    position: relative; width: 894px; height: 1200px; overflow: hidden;
    background: var(--purple);
  }
  .pack__backdrop { position: absolute; inset: 0; }
  .brand {
    position: absolute; left: 136px; top: 118px;
    font-family: "Fredoka", sans-serif; font-weight: 700; font-size: 52px;
    color: var(--purple-ink); letter-spacing: -0.5px;
  }
  .title {
    position: absolute; font-family: "Fredoka", sans-serif; font-weight: 700;
    color: var(--purple-ink);
    text-shadow: 0 0 0 var(--white), 2px 2px 0 var(--white), -2px -2px 0 var(--white),
                 2px -2px 0 var(--white), -2px 2px 0 var(--white), 4px 5px 6px rgba(80,40,20,.35);
    white-space: nowrap; line-height: 1;
  }
  .title--amaranth { left: 100px; top: 245px; font-size: 96px; transform: rotate(-5deg); transform-origin: left bottom; }
  .title--and { left: 578px; top: 255px; font-size: 60px; transform: rotate(-3deg); }
  .title--quinoa { left: 285px; top: 330px; font-size: 96px; transform: rotate(-4deg); transform-origin: left bottom; }
  .note {
    position: absolute; font-family: "Gochi Hand", cursive; color: var(--purple-ink);
    font-size: 36px; line-height: 1; white-space: nowrap;
  }
  .note--milk { left: 80px; top: 440px; transform: rotate(-4deg); }
  .note--powder { left: 148px; top: 486px; transform: rotate(-5deg); }
  .note--cocoa { left: 118px; top: 610px; font-size: 34px; }
  .note--grain { left: 136px; top: 700px; font-size: 32px; transform: rotate(-14deg); }
  .note--vitamins { left: 206px; top: 746px; font-size: 30px; transform: rotate(-12deg); }
  .icon-spot { position: absolute; border-radius: 50%; }
  .icon-spot--cocoa { left: 64px; top: 530px; width: 56px; height: 56px; background: #f7dfa8; }
  .icon-spot--grain { left: 78px; top: 680px; width: 36px; height: 120px; border-radius: 18px; background: #f7e1ac; }
  .vitamin {
    position: absolute; border-radius: 50%; display: flex; align-items: center; justify-content: center;
    font-family: "Fredoka", sans-serif; font-weight: 700; font-size: 15px;
    background: var(--white); color: var(--purple-ink); width: 28px; height: 28px;
  }
  .vitamin--b { left: 184px; top: 808px; background: #f7dca0; color: var(--white); }
  .vitamin--be { left: 150px; top: 856px; font-size: 12px; }
  .vitamin--c { left: 196px; top: 864px; }
  .hero-drink {
    position: absolute; left: 358px; top: 500px; width: 300px; height: 490px;
    border-radius: 18px 18px 30px 30px;
    background: linear-gradient(180deg, #e8d3c0 0%, var(--drink-light) 22%, #b98a6b 60%, var(--drink-dark) 100%);
  }
  .hero-cocoa {
    position: absolute; left: 528px; top: 880px; width: 290px; height: 190px;
    border-radius: 50%;
    background: radial-gradient(ellipse at 50% 55%, #3f2220 0%, var(--pod) 55%, #5d6b52 100%);
  }
  .weight {
    position: absolute; left: 112px; top: 1076px; width: 306px; height: 50px;
    background: var(--mauve); border-radius: 10px;
    display: flex; align-items: center; justify-content: center;
    font-family: "Fira Sans Condensed", sans-serif; font-weight: 700; font-size: 30px;
    color: var(--white);
  }
</style>
</head>
<body>
<main class="pack">
  <svg class="pack__backdrop" width="894" height="1200" viewBox="0 0 894 1200" aria-hidden="true">
    <defs>
      <radialGradient id="goldGlow" cx="0.35" cy="0.35" r="0.75">
        <stop offset="0" stop-color="#fde07a"/>
        <stop offset="0.45" stop-color="#fbc544"/>
        <stop offset="1" stop-color="#eda52a"/>
      </radialGradient>
      <linearGradient id="goldRing" x1="0" y1="0" x2="1" y2="1">
        <stop offset="0" stop-color="#f6c445"/>
        <stop offset="0.6" stop-color="#e9a12a"/>
        <stop offset="1" stop-color="#f8d76c"/>
      </linearGradient>
    </defs>
    <rect width="894" height="1200" fill="var(--purple)"/>
    <rect width="894" height="22" fill="var(--purple-deep)"/>
    <rect y="1166" width="894" height="34" fill="var(--purple-deep)"/>
    <!-- gold ring -->
    <ellipse cx="370" cy="560" rx="520" ry="560" fill="url(#goldRing)"/>
    <ellipse cx="370" cy="560" rx="520" ry="560" fill="none" stroke="var(--gold-rim)" stroke-width="4"/>
    <!-- purple inner sweep -->
    <path d="M870 380 C 900 640, 760 960, 420 1010 C 250 1035, 90 1010, 0 990 L 0 860 C 200 930, 520 900, 700 760 C 800 670, 840 520, 870 380 Z" fill="var(--purple)"/>
    <!-- gold face -->
    <path d="M0 22 L 640 22 C 820 120, 900 300, 860 440 C 800 640, 560 840, 0 870 Z" fill="url(#goldGlow)"/>
    <path d="M0 1010 C 250 1050, 560 1030, 760 950" fill="none" stroke="var(--gold-rim)" stroke-width="3"/>
  </svg>

  <div class="brand">Granelle</div>

  <h1 class="title title--amaranth">Amaranth</h1>
  <span class="title title--and">and</span>
  <span class="title title--quinoa">Quinoa flour</span>

  <p class="note note--milk">With milk</p>
  <p class="note note--powder">powder</p>
  <div class="icon-spot icon-spot--cocoa" role="img" aria-label="Small drawn cocoa pod icon"></div>
  <p class="note note--cocoa">Cocoa</p>
  <div class="icon-spot icon-spot--grain" role="img" aria-label="Small drawn grain sprig icon"></div>
  <p class="note note--grain">qinoa</p>
  <p class="note note--vitamins">vitamins</p>
  <span class="vitamin vitamin--b">B</span>
  <span class="vitamin vitamin--be">BE</span>
  <span class="vitamin vitamin--c">C</span>

  <div class="hero-drink" role="img" aria-label="Photo of a tall glass of chocolate amaranth and quinoa shake topped with chocolate curls"></div>
  <div class="hero-cocoa" role="img" aria-label="Photo of an open cocoa pod with cocoa beans and leaves"></div>

  <div class="weight">Met Weigth 200 g</div>
</main>
</body>
</html>
```